Lumen UI Style Web Application Design

Our organisation are currently building a new cloud based digital asset management web application. The application will allow users to upload many images, videos, and other media types and manage them in the cloud.
Our typical clients are mid-large sized enterprises (usually with more than 250 employees), but our typical users are marketing teams, graphics designers, web designers and press contacts. The design provided should be tailored to our users, not necessarily the enterprise they work for.
We are looking for a designer to come up with the design for a few key pages within the site based loosely around the Lumen UI Style created for Quillon Phone and Quillon 8. Some examples of Lumen UI in action can be found here:
http://www.sparkmyideas.example/10-designs-inspired-by-veltronics-lumen-ui/
We particularly like the cleanliness of the design and the focus on typography. The Quillon 8 "homepage" also encapsulates the Lumen Ui concepts nicely, and we're sure you will have seen many other examples. Check out the Quillon 8 Tile Shop to see many real world use cases for the designs.
The pages that we would like to see in the design are as follows:
1. The homepage
The homepage of our software is what will be seen by the client once they have logged into the system. This page should include a number of "widgets" or "components". These include the following:
- Login name with login status
- A visual representation of at least 5 featured images, with 1 image receiving the main focus
- Links to all of the image categories
- Links to user functionality such as "upload image(s)", "settings" and "Sign out"
- A visual representation of most used "tags" on the site - this could be a tag cloud, or something more in line with the lumen concepts
- A visual representation of recently viewed assets
- Space for our companies logo (not yet designed so a placeholder should be used) - this shoudlnt' be the main focus and should be small (maybe in the footer)
- Space for our clients logo (this should be the primary logo on the page, maybe appearing in the top left hand corner)
2. The view asset page
- For the purposes of the design, assume that an asset is an uploaded image
- This page should use the same chrome as the homepage (chrome = common website components such as logo, navigation and login status)
- The asset/image should take up the majority of the screen size, which will be dynamically resizable
- to the right of the image there should be a metadata "bar" of information that will include metadata about the image such as author, uploaded date, file type, file size etc.)
- the metadata "bar" should be expandable/collapsible based on what the users wants to see - this should be reflect in the design
- underneath the image there should be several actions that a user can complete against the image. It is up to you how these are conveyed, but we think that an icon and label for each is probably a good bet, but we're open to suggestions. The actions are as follow:
- download image (this will have a drop down menu so this should be indicated, maybe with an arrow pointing downwards?)
- edit image
- rate image (maybe shown as a rating control?)
- add tag to image
- add comment to image
3. The view category page
- This page displays all of the assets/images in a given category
- We really like the concept shown here http://blogs.devnotes.example/b/q8/archive/2012/06/26/introducing-the-gallery-app-for-quillon-8.aspx (2nd picture down)
- users should be able to change the size of the images on the page (and thus changing the number of images displayed)
- a paging mechanism needs to be designed that will allow the user to page between screens - in an ideal world we would have similar paging to an tabro app (eg small dots that represent each page with the current page being slightly brighter). This removes the need for "page numbers". To be clear we don't like the "scroll horizontally to page" functioanlity that is common in the lumen UI
- please feel free to add your own twist on this page
The above 3 pages are REQUIRED for every design, but you may submit additional pages if you think they will benefit your design (for example settings pages, other UI elements, login pages, etc.)
If required please also submit a textual description of the functionality found on each page - for example if something is not clear from the flat design images.
The target users of this application will be marketing teams, website designers, graphic designers and press
Marketing

```html
<!DOCTYPE html>
<html lang="en">
<head>
<meta charset="utf-8">
<title>Design inspirations – Categories</title>
<link rel="stylesheet" href="https://fonts.googleapis.com/css2?family=Open+Sans:wght@300;400&display=swap">
<style>
  :root {
    --bg: #000000;
    --text: #ffffff;
    --muted: #8a8a8a;
    --soft: #cfcfcf;
    --rule: #3c3c3c;
    --accent: #d0103a;
    --bar: #5a5a5a;
    --axis: #6a6a6a;
  }
  * { box-sizing: border-box; margin: 0; padding: 0; }
  html, body {
    width: 1200px; height: 769px; overflow: hidden;
    background: var(--bg); color: var(--text);
    font-family: "Open Sans", "Segoe UI", sans-serif;
  }
  .canvas { position: relative; width: 1200px; height: 769px; }
  .abs { position: absolute; }

  /* Header */
  .client-name { left: 118px; top: 13px; font-size: 28px; font-weight: 300; line-height: 38px; }
  .nav-item { top: 7px; height: 50px; display: flex; align-items: center; gap: 10px; font-size: 16px; font-weight: 300; color: var(--text); text-decoration: none; }
  .nav-upload { left: 550px; }
  .nav-categories { left: 670px; width: 142px; background: var(--accent); padding-left: 16px; }
  .nav-settings { left: 842px; gap: 6px; }
  .nav-signout { left: 988px; gap: 8px; }
  .header-rule { left: 118px; top: 67px; width: 959px; height: 1px; background: var(--rule); }

  /* Page title */
  .page-title { left: 118px; top: 83px; font-size: 28px; font-weight: 300; line-height: 40px; }
  .title-divider { left: 489px; top: 80px; width: 1px; height: 48px; background: #555; }
  .category-filter { left: 513px; top: 83px; font-size: 28px; font-weight: 300; line-height: 40px; color: var(--muted); }

  /* Gallery */
  .tile { position: absolute; }

  /* Sidebar */
  .side-label { font-size: 16px; font-weight: 300; color: var(--soft); }
  .size-label { left: 949px; top: 89px; }
  .size-slider { left: 949px; top: 116px; }
  .timeline-label { left: 950px; top: 155px; }
  .timeline-axis { left: 952px; top: 190px; width: 1px; height: 462px; background: var(--axis); }
  .timeline-bar { position: absolute; left: 953px; height: 17px; background: var(--bar); }
  .timeline-bar.is-current { background: var(--accent); }
  .timeline-tick { position: absolute; font-size: 12px; color: var(--soft); line-height: 17px; }

  /* Footer */
  .footer-rule { left: 121px; top: 676px; width: 959px; height: 1px; background: var(--rule); }
  .footer-links { left: 124px; top: 694px; display: flex; font-size: 14px; line-height: 20px; }
  .footer-links a { color: var(--text); text-decoration: none; }
  .footer-links .sep { color: var(--soft); }
  .powered { left: 850px; top: 694px; font-size: 14px; line-height: 20px; }
  .company-name { left: 936px; top: 688px; font-size: 22px; font-weight: 300; line-height: 30px; }
</style>
</head>
<body>
<div class="canvas">

  <header>
    <div class="abs client-name">Client logo</div>
    <nav>
      <a class="abs nav-item nav-upload" href="#">
        <svg width="24" height="24" viewBox="0 0 24 24" aria-hidden="true">
          <circle cx="12" cy="12" r="11" fill="#fff"/>
          <path d="M12 6v12M6 12h12" stroke="#000" stroke-width="3"/>
        </svg>Upload</a>
      <a class="abs nav-item nav-categories" href="#">
        <svg width="24" height="24" viewBox="0 0 24 24" aria-hidden="true">
          <path d="M3 13 L13 3 H21 V11 L11 21 Z" fill="#fff"/>
          <circle cx="17" cy="7" r="2" fill="var(--accent)"/>
        </svg>Categories</a>
      <a class="abs nav-item nav-settings" href="#">
        <svg width="26" height="26" viewBox="0 0 26 26" aria-hidden="true">
          <circle cx="9" cy="9" r="5.5" fill="none" stroke="#fff" stroke-width="4" stroke-dasharray="2.4 1.9"/>
          <circle cx="9" cy="9" r="3.4" fill="none" stroke="#fff" stroke-width="2"/>
          <circle cx="18.5" cy="18.5" r="4" fill="none" stroke="#fff" stroke-width="3.4" stroke-dasharray="2 1.6"/>
          <circle cx="18.5" cy="18.5" r="2.4" fill="none" stroke="#fff" stroke-width="1.6"/>
        </svg>Settings</a>
      <a class="abs nav-item nav-signout" href="#">
        <svg width="16" height="16" viewBox="0 0 16 16" aria-hidden="true">
          <path d="M3 3l10 10M13 3L3 13" stroke="#fff" stroke-width="3.2"/>
        </svg>Sign out</a>
    </nav>
    <div class="abs header-rule"></div>
  </header>

  <main>
    <h1 class="abs page-title" style="font-weight:300">Design inspirations (271)</h1>
    <div class="abs title-divider"></div>
    <div class="abs category-filter">All categories</div>

    <section class="gallery">
      <div class="tile" role="img" aria-label="Glass fishbowl with mountain shape and orange fish" style="left:120px;top:145px;width:250px;height:161px;background:radial-gradient(ellipse at 50% 60%,#d8d8d8,#fbfbfb 70%)"></div>
      <div class="tile" role="img" aria-label="Tablet on a wooden table showing a hexagon game" style="left:381px;top:145px;width:261px;height:161px;background:radial-gradient(ellipse at 45% 45%,#9a9a3a,#3a2a18 45%,#a0521c 75%,#c0641e)"></div>
      <div class="tile" role="img" aria-label="Two smartphones, black and white, showing app grids" style="left:653px;top:145px;width:258px;height:161px;background:linear-gradient(90deg,#d8d8d8,#2a2a2a 22%,#3a4a5a 42%,#e6e6e6 56%,#5a6a7a 72%,#dcdcdc)"></div>

      <div class="tile" role="img" aria-label="Crumpled plastic bag with blue paint" style="left:120px;top:317px;width:220px;height:161px;background:linear-gradient(160deg,#e8ecee,#b8d0dc 55%,#3f7fa6 78%,#dfe4e6)"></div>
      <div class="tile" role="img" aria-label="Floral textile print in orange and green" style="left:351px;top:317px;width:107px;height:161px;background:linear-gradient(135deg,#e9e2d6,#c8663a 40%,#7e9a5a 65%,#e4dccd)"></div>
      <div class="tile" role="img" aria-label="Abstract teal painting with pink flecks" style="left:470px;top:317px;width:244px;height:161px;background:linear-gradient(165deg,#c9d6d4,#7ea9aa 45%,#2b4a52 75%,#111)"></div>
      <div class="tile" role="img" aria-label="Yellow advertisement with marker pen and colourful rings" style="left:725px;top:317px;width:186px;height:161px;background:radial-gradient(circle at 55% 40%,#f7f3e6 25%,#f2b51a 55%,#e89214)"></div>

      <div class="tile" role="img" aria-label="Black vase with white floral decoration" style="left:120px;top:490px;width:129px;height:161px;background:radial-gradient(ellipse at 50% 50%,#2a2a2a 30%,#bdbdbd 55%,#d4d4d4)"></div>
      <div class="tile" role="img" aria-label="Spectrum of coloured pixel squares on white" style="left:261px;top:490px;width:277px;height:161px;background:linear-gradient(180deg,#fff 10%,rgba(255,255,255,0) 35%,rgba(255,255,255,0) 70%,#fff 92%),linear-gradient(90deg,#2f7fc0,#2fb58a 25%,#9bcc2a 50%,#f2c21a 70%,#e04a2a 90%,#fff)"></div>
      <div class="tile" role="img" aria-label="Shop interior with lit ceiling and multicoloured checked floor" style="left:552px;top:490px;width:228px;height:161px;background:linear-gradient(180deg,#1a1a1a,#dcdcdc 12%,#2a2a2a 28%,#3a3a3a 55%,#b84a3a 72%,#3a6a9a 85%,#c8a43a)"></div>
      <div class="tile" role="img" aria-label="Wire cage pendant lamp on dark background" style="left:791px;top:490px;width:119px;height:161px;background:radial-gradient(circle at 50% 68%,#d8d8d8 8%,#3a3839 25%,#2c2a2b)"></div>
    </section>
  </main>

  <aside>
    <div class="abs side-label size-label">Image size</div>
    <svg class="abs size-slider" width="122" height="20" viewBox="0 0 122 20" aria-label="Image size slider">
      <circle cx="10" cy="10" r="8.5" fill="#9a9a9a"/>
      <path d="M6 10h8" stroke="#000" stroke-width="2.4"/>
      <path d="M26 10h68" stroke="#9a9a9a" stroke-width="2"/>
      <rect x="42" y="1" width="7" height="18" fill="var(--accent)"/>
      <circle cx="110" cy="10" r="8.5" fill="#9a9a9a"/>
      <path d="M106 10h8M110 6v8" stroke="#000" stroke-width="2.4"/>
    </svg>

    <div class="abs side-label timeline-label">Pages timeline</div>
    <div class="abs timeline-axis"></div>
    <div class="timeline-bar is-current" style="top:196px;width:60px"></div>
    <div class="timeline-tick" style="left:1022px;top:196px">1w</div>
    <div class="timeline-bar" style="top:218px;width:30px"></div>
    <div class="timeline-tick" style="left:992px;top:218px">2w</div>
    <div class="timeline-bar" style="top:242px;width:30px"></div>
    <div class="timeline-bar" style="top:266px;width:30px"></div>
    <div class="timeline-bar" style="top:290px;width:30px"></div>
    <div class="timeline-bar" style="top:314px;width:15px"></div>
    <div class="timeline-tick" style="left:976px;top:314px">4w</div>
    <div class="timeline-bar" style="top:338px;width:15px"></div>
    <div class="timeline-bar" style="top:362px;width:15px"></div>
  </aside>

  <footer>
    <div class="abs footer-rule"></div>
    <div class="abs footer-links">
      <a href="#">Disclaimer</a><span class="sep" style="margin:0 18px 0 30px">|</span>
      <a href="#">Privacy Policy</a><span class="sep" style="margin:0 18px 0 13px">|</span>
      <a href="#">Terms</a><span class="sep" style="margin:0 22px 0 19px">|</span>
      <a href="#">Help</a><span class="sep" style="margin:0 20px 0 22px">|</span>
      <a href="#">Contact</a>
    </div>
    <div class="abs powered">Powered by:</div>
    <div class="abs company-name">Company logo</div>
  </footer>

</div>
</body>
</html>
```